IT Network Consultancy - Business Card

t4 linkways is a IT network consultancy based in London. We're looking for a smart, modern and professional business card design. Our website is here: www.t4linkways.co.uk

Key things that should be included on the card (with examples):

Company Logo
Name
Position / Job Title: Network Consultant
Mobile Phone Number: +44 (0) 7700 900418
Land Line: +44 (0) 1632 960274
Email Address: name@t4linkways.co.uk
Web Site URL: www.t4linkways.co.uk

Target Market(s)

Large enterprise / global companies / corporates

Industry/Entity Type

Business

Requirements
Must have
• Incorporate our logo - which is attached to the project. They are in AI format (can be opened in Inkscape).

The design should be double sided and fit on a UK standard 85mm × 55mm card and be in a format that retains the quality when printed.
Nice to have
• The project does not have to conform to the colour of our website but this should give you inspiration of the style we like.
Should not have
• Bright colours. Pictures are not necessary.

```html
<!DOCTYPE html>
<html lang="en">
<head>
<meta charset="utf-8">
<title>t4 linkways – Business Card</title>
<link href="https://fonts.googleapis.com/css2?family=Michroma&display=swap" rel="stylesheet">
<style>
  :root {
    --page: #ffffff;
    --card-back: #5e6870;
    --card-back-shade: #525c64;
    --card-front-light: #868d93;
    --card-front-dark: #4b545b;
    --ink: #ffffff;
    --ink-soft: #e6e9eb;
  }
  * { margin: 0; padding: 0; box-sizing: border-box; }
  html, body {
    width: 1200px;
    height: 461px;
    overflow: hidden;
    background: var(--page);
  }
  body {
    position: relative;
    font-family: "Michroma", sans-serif;
    color: var(--ink);
  }
  .card {
    position: absolute;
    top: 61px;
    width: 527px;
    height: 339px;
    border-radius: 26px;
    overflow: hidden;
  }
  .card--contact {
    left: 61px;
    background: linear-gradient(160deg, var(--card-back) 0%, var(--card-back) 55%, var(--card-back-shade) 100%);
  }
  .card--brand {
    left: 620px;
    background: radial-gradient(ellipse 60% 65% at 42% 48%, var(--card-front-light) 0%, #6a7279 45%, var(--card-front-dark) 100%);
  }
  .contact {
    position: absolute;
    left: 0;
    width: 100%;
    top: 100px;
    padding-left: 20px;
    text-align: center;
  }
  .contact__name {
    font-size: 21px;
    letter-spacing: 0.5px;
    line-height: 1;
  }
  .contact__role {
    margin-top: 6px;
    font-size: 15px;
    text-transform: lowercase;
    line-height: 1;
    color: var(--ink-soft);
  }
  .contact__details {
    margin-top: 22px;
    font-size: 12px;
    line-height: 15px;
    text-transform: lowercase;
  }
  .contact__web {
    margin-top: 18px;
    font-size: 12.5px;
    text-transform: lowercase;
  }
  .brand {
    position: absolute;
    left: 0;
    width: 100%;
    top: 62px;
    text-align: center;
  }
  .brand__mark {
    font-size: 104px;
    line-height: 1;
    letter-spacing: 2px;
  }
  .brand__word {
    margin-top: 20px;
    font-size: 38px;
    line-height: 1;
    letter-spacing: 1px;
  }
  .brand__tagline {
    margin-top: 12px;
    font-size: 7.5px;
    letter-spacing: 0.2px;
    text-transform: lowercase;
    color: var(--ink-soft);
  }
</style>
</head>
<body>
  <section class="card card--contact" aria-label="Card reverse: contact details">
    <div class="contact">
      <p class="contact__name">DANIEL MARSH</p>
      <p class="contact__role">Network Consultant</p>
      <div class="contact__details">
        <p>Mobile: +44 (0) 7700 900418</p>
        <p>Phone:&nbsp; +44 (0) 1632 960274</p>
        <p>E-mail:&nbsp; name@t4linkways.co.uk</p>
      </div>
      <p class="contact__web">www.t4linkways.co.uk</p>
    </div>
  </section>

  <section class="card card--brand" aria-label="Card front: company name">
    <div class="brand">
      <p class="brand__mark">T4</p>
      <p class="brand__word">LINKWAYS</p>
      <p class="brand__tagline">IT Networking and Network Security Solutions</p>
    </div>
  </section>
</body>
</html>
```